Business Cards Design for the electrical wholesaler: clean bold dynamic :)

We need a business card design that would follow our latest brand guidelines. As an electrical wholesaler we want to bring a fresh look and feel into the industry. The design should be clean bold and dynamic. It should come alive with the renewed energy of our green colour. Our grey colour should keep things balanced and complement the notion of maturity and responsibility. We employ Lato as a corporate font however are not bound by this font and we’re open to interpretation here.

Target Market(s)

Electrical contractors

Industry/Entity Type

Business

Contact Information for Business Card

Logo
Name & Surname: Olena Dovbush
Job Title: Director of Marketing
Email: helen.dovbush@mailvane.example
Cell phone: XXX.XXX.XXXX
Address: 20917 - 87 Ave. Edmonton, AB, Canada. T6K 2R8
Business Phone: 780.555.0187
Website: www.qorvil.example

Font styles to use
Other font styles liked:
• Lato

Requirements
Must have
• Logo & website
Nice to have
• Brand elements - some of them you may find in the attached Brand Guidelines (e.g. three lines on the background signifying "W")

```html
<!DOCTYPE html>
<html lang="en">
<head>
<meta charset="utf-8">
<title>Qorvil Electrical Wholesalers – Business Cards</title>
<link rel="stylesheet" href="https://fonts.googleapis.com/css2?family=Lato:wght@400;700;900&display=swap">
<style>
  :root {
    --green: #8fd640;
    --grey: #3c3d3f;
    --ink: #4a4b4d;
    --paper: #ffffff;
    --backdrop: #4d4d4f;
  }
  * { box-sizing: border-box; margin: 0; padding: 0; }
  html, body { width: 1200px; height: 1200px; overflow: hidden; }
  body {
    background: var(--backdrop);
    font-family: "Lato", Arial, sans-serif;
    color: var(--ink);
    position: relative;
  }
  .card {
    position: absolute;
    left: 160px;
    width: 880px;
    height: 503px;
    background: var(--paper);
    overflow: hidden;
    box-shadow: 0 10px 30px rgba(0,0,0,.35);
  }
  .card--front { top: 68px; }
  .card--back  { top: 629px; }
  .card__shapes { position: absolute; inset: 0; width: 100%; height: 100%; }
  .shape--green { fill: var(--green); }
  .shape--grey  { fill: var(--grey); }

  .brand { position: absolute; display: flex; align-items: center; }
  .brand__mark { background: var(--green); flex: none; }
  .brand__name { font-weight: 700; color: var(--ink); line-height: 1; letter-spacing: -1px; }
  .brand__tagline {
    position: absolute; font-weight: 700; text-transform: uppercase;
    color: var(--ink); letter-spacing: 3px;
  }

  .card--front .brand { left: 150px; top: 190px; gap: 20px; }
  .card--front .brand__mark { width: 62px; height: 62px; }
  .card--front .brand__name { font-size: 118px; }
  .card--front .brand__tagline { left: 232px; top: 306px; font-size: 17px; }

  .card--back .brand { left: 70px; top: 78px; gap: 12px; }
  .card--back .brand__mark { width: 34px; height: 34px; }
  .card--back .brand__name { font-size: 64px; }

  .holder {
    position: absolute; right: 40px; top: 160px; text-align: right; color: var(--paper);
  }
  .holder__name { font-size: 36px; font-weight: 900; line-height: 1.1; }
  .holder__title { font-size: 17px; font-weight: 400; margin-top: 2px; }

  .contacts { position: absolute; left: 500px; top: 300px; list-style: none; font-size: 17px; line-height: 1.35; }
  .contacts__item { display: flex; gap: 10px; align-items: flex-start; margin-bottom: 6px; }
  .contacts__item--address { margin-bottom: 26px; }
  .contacts__icon { flex: none; width: 18px; height: 18px; margin-top: 2px; }
  .contacts__icon circle { fill: var(--green); }
  .contacts__icon path { fill: none; stroke: var(--paper); stroke-width: 1.6; stroke-linecap: round; stroke-linejoin: round; }
</style>
</head>
<body>

<section class="card card--front" aria-label="Card front">
  <svg class="card__shapes" viewBox="0 0 880 503" aria-hidden="true">
    <polygon class="shape--green" points="360,0 700,0 600,165 260,165"/>
    <polygon class="shape--grey" points="520,345 840,345 740,503 420,503"/>
  </svg>
  <div class="brand">
    <span class="brand__mark"></span>
    <span class="brand__name">qorvil</span>
  </div>
  <span class="brand__tagline">Electrical Wholesalers</span>
</section>

<section class="card card--back" aria-label="Card back">
  <svg class="card__shapes" viewBox="0 0 880 503" aria-hidden="true">
    <polygon class="shape--grey" points="0,185 310,185 360,440 0,440" transform="translate(0,0)"/>
    <polygon class="shape--green" points="470,140 880,140 880,262 440,262"/>
  </svg>
  <div class="brand">
    <span class="brand__mark"></span>
    <span class="brand__name">qorvil</span>
  </div>

  <div class="holder">
    <p class="holder__name">Olena Dovbush</p>
    <p class="holder__title">Director of Marketing</p>
  </div>

  <ul class="contacts">
    <li class="contacts__item contacts__item--address">
      <svg class="contacts__icon" viewBox="0 0 18 18" aria-hidden="true"><circle cx="9" cy="9" r="9"/><path d="M9 14c-2.5-3-3.5-4.5-3.5-6a3.5 3.5 0 0 1 7 0c0 1.5-1 3-3.5 6z"/></svg>
      <span>20917 - 87 Ave.<br>Edmonton, AB, Canada.<br>T6K 2R8</span>
    </li>
    <li class="contacts__item">
      <svg class="contacts__icon" viewBox="0 0 18 18" aria-hidden="true"><circle cx="9" cy="9" r="9"/><path d="M6 5l2 2-1 1.5a6 6 0 0 0 2.5 2.5L11 10l2 2-1.5 1.5C8 13 5 10 4.5 6.5z"/></svg>
      <span>XXX.XXX.XXXX</span>
    </li>
    <li class="contacts__item">
      <svg class="contacts__icon" viewBox="0 0 18 18" aria-hidden="true"><circle cx="9" cy="9" r="9"/><path d="M4.5 6h9v6h-9zM4.5 6L9 9.5 13.5 6"/></svg>
      <span>helen.dovbush@mailvane.example</span>
    </li>
    <li class="contacts__item">
      <svg class="contacts__icon" viewBox="0 0 18 18" aria-hidden="true"><circle cx="9" cy="9" r="9"/><path d="M9 4a5 5 0 1 0 0 10A5 5 0 1 0 9 4zM4 9h10M9 4c-2 3-2 7 0 10M9 4c2 3 2 7 0 10"/></svg>
      <span>www.qorvil.example</span>
    </li>
  </ul>
</section>

</body>
</html>
```